Copper Lantern: A Self Care Session for Employees

I need a flyer for organizations and businnesses. I am offering a session that will address behavioral issues such as coming to work late, not getting along with others and not working together as a team. I am a life coach who works with difficult employees, helping them address their issues and helping them be a better version of themselves. I also offer a leadership class for managers. I would like the flyer to be professional, clean and convey a feeling of trust. I would prefer to see disgns that use the color blue.

Target Market(s)

small businesses

Industry/Entity Type

Work

Font styles to use
Sans Serif

Colors
34a7d8
85cae6
0792cd
ffffff

Requirements
Must have
• shades of blue and perhaps white. should be clean, fresh and professional
Nice to have
• simple yet warm
Should not have
• distracting and heavy, playful

```html
<!DOCTYPE html>
<html lang="en">
<head>
<meta charset="utf-8">
<title>Copper Lantern: A Self Care Session for Employees</title>
<link href="https://fonts.googleapis.com/css2?family=Roboto+Condensed:wght@300;400;700;900&display=swap" rel="stylesheet">
<style>
  :root {
    --blue-deep: #0792cd;
    --blue-mid: #34a7d8;
    --blue-light: #85cae6;
    --white: #ffffff;
    --ink: #2a2a2a;
    --navy: #1c2c47;
  }
  * { margin: 0; padding: 0; box-sizing: border-box; }
  html, body { width: 768px; height: 1200px; overflow: hidden; background: var(--white); }
  .flyer {
    position: relative; width: 768px; height: 1200px; overflow: hidden;
    background: var(--white);
    font-family: "Roboto Condensed", Arial, sans-serif; color: var(--ink);
  }
  .hero-photo {
    position: absolute; right: 0; top: 0; width: 420px; height: 1200px;
    background:
      linear-gradient(90deg, var(--white) 0%, rgba(255,255,255,0) 30%),
      radial-gradient(ellipse 55% 22% at 70% 24%, #6b4431 0%, #4a2e22 60%, rgba(74,46,34,0) 100%),
      linear-gradient(180deg, #f2f2f2 0%, #e9ebee 35%, #2b3d5e 52%, #1f2f4c 80%, #17243c 100%);
  }
  .headline { position: absolute; left: 32px; top: 52px; }
  .headline .lead { font-size: 31px; font-weight: 400; }
  .headline .personal {
    font-size: 92px; font-weight: 900; color: var(--blue-deep);
    line-height: 0.95; margin-top: 12px; letter-spacing: -1px;
  }
  .headline .issues {
    font-size: 128px; font-weight: 900; color: var(--blue-light);
    line-height: 0.95; letter-spacing: -1px;
  }
  .headline .job { font-size: 48px; font-weight: 400; margin-top: 14px; }
  .points { position: absolute; left: 32px; top: 458px; list-style: none; width: 390px; }
  .points li {
    position: relative; padding-left: 26px; font-size: 22px; line-height: 1.3; margin-bottom: 28px;
  }
  .points li::before {
    content: ""; position: absolute; left: 2px; top: 9px; width: 11px; height: 11px;
    border-radius: 50%; background: var(--blue-deep);
  }
  .brand {
    position: absolute; left: 34px; top: 660px; display: flex; align-items: center; gap: 14px;
  }
  .brand .dot { width: 46px; height: 46px; border-radius: 50%; background: var(--blue-mid); }
  .brand .name {
    font-size: 30px; font-weight: 400; color: var(--blue-deep); line-height: 1.1;
  }
  .coach {
    position: absolute; left: 10px; top: 880px; width: 300px; height: 300px;
    border-radius: 50%; background: #d6ecf7; padding: 14px;
  }
  .coach-photo {
    width: 100%; height: 100%; border-radius: 50%; overflow: hidden; position: relative;
    border: 4px solid var(--blue-light);
    background:
      radial-gradient(ellipse 60% 45% at 50% 85%, #1e4fd6 0%, #1b45c0 60%, rgba(27,69,192,0) 100%),
      linear-gradient(180deg, #eef4f8 0%, #d9e4ec 100%);
  }
  .coach-label {
    position: absolute; left: 50px; bottom: 34px; color: var(--white); text-align: center;
  }
  .coach-label .coach-name { font-size: 21px; font-weight: 700; }
  .coach-label .coach-role { font-size: 9px; line-height: 1.2; }
  .session-band {
    position: absolute; left: 300px; top: 952px; width: 468px; height: 74px;
    background: var(--blue-deep); color: var(--white); padding: 10px 0 0 20px;
    font-size: 24px; line-height: 1.3; text-transform: uppercase;
  }
  .contact-band {
    position: absolute; left: 300px; top: 1026px; width: 468px; height: 76px;
    background: var(--blue-light); padding: 10px 0 0 20px; color: var(--navy);
  }
  .contact-band .intro { font-size: 14px; }
  .contact-band .intro b { font-weight: 700; }
  .contact-band .phones { font-size: 26px; font-weight: 700; margin-top: 2px; }
  .contact-band .phones span { font-weight: 400; }
</style>
</head>
<body>
<main class="flyer">
  <div class="hero-photo" role="img" aria-label="Photo of a stressed businessman in a navy suit, eyes closed, hand to his forehead"></div>

  <header class="headline">
    <p class="lead">Are your employees bringing</p>
    <h1><span class="personal" style="display:block">PERSONAL</span><span class="issues" style="display:block">ISSUES</span></h1>
    <p class="job">ON THE JOB?</p>
  </header>

  <ul class="points">
    <li>Is it affecting team communication or may be even productivity?</li>
    <li>If the behavior of an employee, manager or your entire staff is a problem I can help.</li>
  </ul>

  <div class="brand">
    <span class="dot"></span>
    <p class="name">Willow Path<br>Life Coaching Institute</p>
  </div>

  <div class="coach">
    <div class="coach-photo" role="img" aria-label="Portrait of the life coach in a blue dress, seated"></div>
    <div class="coach-label">
      <p class="coach-name">MARISOL KENT</p>
      <p class="coach-role">C.E.O. Certified Life Coach<br>and host of a coaching show</p>
    </div>
  </div>

  <div class="session-band">
    <p>Copper Lantern:</p>
    <p>A Self Care Session for Employees</p>
  </div>
  <div class="contact-band">
    <p class="intro">For more information contact <b>MARISOL KENT</b> on</p>
    <p class="phones">242-555-0148 <span>or</span> 555-0192</p>
  </div>
</main>
</body>
</html>
```